National Virtual accounting firm needs website designed

I need a wordpress website design for a national virtual accounting firm. I will upload my business card, logo, and postcards that I have had designed and followed the same style. I want a similar style to be followed so I can keep the running theme similar.

Services include:

Tax Services:
Tax preparation and planning services for Individuals, businesses, estates, and nonprofits
Full Service Payroll for Businesses
QVT Audit Representation

Consulting:
Entity Selection & Restructuring
Financial Projections & Forecasts
Retirement Planning
IPO Readiness

Accounting:
Bookkeeping
Reviews and Compilations
Payroll Services

Other Services:
CFO Services
Compliance Services
Controller Services
Software Implementations for Tenvolk, Brombalt, and Plovena.

Target Market(s)

small to medium size businesses, and individuals

Industry/Entity Type

accounting firms

Font styles to use
Sans Serif

Colors
59FF00
82FF00
B8FF75
E3FFCB
F4FFEA

Requirements
Must have
• Color schematics from the logo and post cards/business cards

```html
<!DOCTYPE html>
<html lang="en">
<head>
<meta charset="utf-8">
<title>Verdano – Virtual Accounting</title>
<link rel="stylesheet" href="https://fonts.googleapis.com/css2?family=Alfa+Slab+One&family=Roboto:wght@400;500;700&display=swap">
<style>
:root{
  --green:#62bb46;
  --green-light:#8fd14f;
  --green-dark:#3f9a2c;
  --yellow:#ffd200;
  --dark:#161616;
  --ink:#222;
  --muted:#555;
  --white:#fff;
}
*{box-sizing:border-box;margin:0;padding:0}
html,body{width:1200px;height:4375px;overflow:hidden}
body{position:relative;background:var(--white);font-family:"Roboto",sans-serif;color:var(--ink)}
.abs{position:absolute}
.slab{font-family:"Alfa Slab One",serif;font-weight:400}
.btn{position:absolute;display:flex;align-items:center;justify-content:center;background:linear-gradient(180deg,var(--green-light),var(--green));color:#1b3a10;font-family:"Alfa Slab One",serif;font-size:16px;border-radius:26px;box-shadow:0 8px 14px rgba(98,187,70,.35)}
/* top bar */
.topbar{left:0;top:0;width:1200px;height:48px;background:linear-gradient(90deg,var(--green),var(--green-light));border-radius:0 0 30px 0}
.topbar .call{left:112px;top:14px;font-size:16px;font-weight:500;color:#0f2a08}
.topbar .consult{right:113px;top:0;width:194px;height:48px;background:var(--yellow);color:#1b2a00;font-weight:700;font-size:16px;display:flex;align-items:center;justify-content:center}
/* hero */
.hero-bg{left:0;top:48px;width:1200px;height:700px;background:radial-gradient(ellipse at 55% 40%,#4a4a3e 0%,#2a2a26 45%,#121212 100%)}
.hero-top{left:0;top:0;width:1200px;height:48px;background:#1a1a18}
.brand{display:flex;align-items:center;gap:10px;font-family:"Alfa Slab One",serif;color:var(--white);font-size:40px;letter-spacing:1px}
.brand .dot{width:30px;height:30px;border-radius:50%;background:var(--yellow)}
.nav{top:108px;left:612px;display:flex;gap:30px;font-size:15px;color:var(--white);font-weight:500}
.nav .active{color:var(--yellow)}
.hero-title{left:0;width:1200px;top:265px;text-align:center;color:var(--white);font-size:33px;line-height:45px}
.hero-title u{text-decoration:none;border-bottom:4px solid var(--green)}
.hero-text{left:280px;width:640px;top:376px;text-align:center;color:var(--white);font-size:16px;line-height:29px}
.hero-btn{left:482px;top:468px;width:236px;height:48px;border:3px solid var(--yellow)}
.dots{left:552px;top:675px;display:flex;gap:16px}
.dots span{width:22px;height:22px;border-radius:50%;border:2px solid #666;background:#fff}
.dots .on{background:var(--yellow);border-color:var(--yellow)}
/* about */
.eyebrow{font-size:20px;font-weight:500;color:var(--ink)}
.about-eyebrow{left:112px;top:820px}
.about-title{left:112px;top:848px;font-size:54px;color:var(--yellow);border-bottom:4px solid var(--green);line-height:60px;padding-right:4px}
.about-text{left:112px;top:935px;width:470px;font-size:14.5px;line-height:25.5px;color:var(--muted)}
.about-text p+p{margin-top:22px}
.about-btn{left:112px;top:1137px;width:185px;height:51px}
.about-photo{border-radius:160px;box-shadow:0 10px 25px rgba(0,0,0,.15)}
/* services */
.services-bg{left:0;top:1290px;width:1200px;height:697px;background:linear-gradient(180deg,#3a3a36,#1d1d1b)}
.services-eyebrow{left:0;width:1200px;top:1440px;text-align:center;color:var(--white)}
.services-title{left:0;width:1200px;top:1466px;text-align:center;color:var(--yellow);font-size:56px}
.services-underline{left:510px;top:1535px;width:180px;height:4px;background:var(--green);border-radius:2px}
.services-text{left:200px;width:800px;top:1568px;text-align:center;color:var(--white);font-size:15px;line-height:27px}
.card{top:1664px;width:304px;height:401px;border-radius:16px;overflow:hidden}
.card .label{position:absolute;left:0;right:0;bottom:34px;display:flex;justify-content:center;align-items:center;gap:26px;color:var(--white);font-size:21px}
.arrow{width:38px;height:38px;border-radius:50%;background:var(--yellow);display:flex;align-items:center;justify-content:center}
.card-consult{background:linear-gradient(180deg,#8bd152,#5ab53e);color:var(--white);text-align:center}
.card-consult h3{font-weight:400;font-size:21px;margin-top:84px;margin-bottom:24px}
.card-consult li{list-style:none;font-size:16px;line-height:30px}
.card-consult .arrow{margin:28px auto 0;width:36px;height:36px}
.services-btn{left:508px;top:2114px;width:184px;height:51px}
/* why + contact */
.why{left:112px;top:2279px;width:488px;height:570px;background:linear-gradient(160deg,#2b2b28,#0e0e0e)}
.why h2{position:absolute;left:42px;top:74px;color:var(--white);font-size:31px;line-height:47px}
.why h2 em{font-style:normal;color:var(--green-light)}
.feature{position:absolute;left:42px;display:flex;align-items:center;gap:20px;color:var(--green-light);font-size:17px}
.feature .ic{width:60px;height:60px;border-radius:50%;background:var(--yellow);display:flex;align-items:center;justify-content:center}
.contact{left:600px;top:2279px;width:488px;height:570px;background:linear-gradient(160deg,#7dcb4a,#5eb63d)}
.contact h3{position:absolute;left:21px;top:112px;color:var(--white);font-weight:500;font-size:24px}
.contact .bar{position:absolute;left:21px;top:161px;width:90px;height:3px;background:var(--yellow)}
.field{position:absolute;height:37px;background:var(--white);border-radius:10px;font-size:12px;color:#666;padding:11px 16px}
.submit{position:absolute;left:21px;top:2664px;width:153px;height:36px;border-radius:18px;background:var(--yellow);font-size:12px;font-weight:700;display:flex;align-items:center;justify-content:center;color:#222}
/* news */
.news-title{left:0;width:1200px;top:2982px;text-align:center;font-size:40px;line-height:58px;color:var(--ink)}
.news-card{top:3136px;background:var(--white);box-shadow:0 8px 22px rgba(0,0,0,.08)}
.news-card .img{height:336px;border-bottom:4px solid var(--green)}
.news-card .date{position:absolute;top:318px;left:50%;transform:translateX(-50%);background:var(--yellow);color:var(--white);font-size:15px;font-weight:500;padding:8px 24px;border-radius:6px 6px 0 0}
.news-card h4{text-align:center;font-weight:500;color:var(--ink);padding:14px 10px 0}
.news-btn{left:508px;top:3698px;width:184px;height:51px}
/* footer */
.footer-bg{left:0;top:3820px;width:1200px;height:555px;background:linear-gradient(180deg,#1d1d1b,#0c0c0c)}
.foot-brand{left:112px;top:4085px}
.foot-col h5{font-size:16px;font-weight:500;color:var(--white);margin-bottom:14px}
.foot-col li{list-style:none;font-size:13px;color:#cfcfcf;line-height:38.5px}
.reach{display:flex;gap:18px;margin-bottom:20px;font-size:12.5px;color:#e6e6e6;line-height:19px}
.reach .ic{flex:none;width:40px;height:40px;border-radius:50%;border:2px solid var(--yellow);display:flex;align-items:center;justify-content:center}
.copyright{left:110px;top:4325px;font-size:12px;color:#bdbdbd}
.social{left:904px;top:4320px;display:flex;gap:20px}
.social span{width:20px;height:20px;border-radius:50%;background:var(--yellow)}
</style>
</head>
<body>

<!-- hero -->
<div class="abs hero-top"></div>
<div class="abs hero-bg" role="img" aria-label="Hands on a laptop keyboard with glowing tax and finance icons overlaid"></div>
<header>
  <div class="abs topbar">
    <div class="abs call">Call Now | (555) 204-3187</div>
    <div class="abs consult">Free Consult Now</div>
  </div>
  <div class="abs brand" style="left:112px;top:82px"><span class="dot"></span>VERDANO</div>
  <nav class="abs nav"><span class="active">Home</span><span>About Us</span><span>What We Do</span><span>Latest News</span><span>Contact Us</span></nav>
</header>
<h1 class="abs hero-title slab">Why Settle for Less<br>When Your <u>Finances Could be Exact?</u></h1>
<p class="abs hero-text">Lorem Ipsum is simply dummy text of the printing and typesetting industry. Lorem Ipsum has been the industry's standard dummy text ever since the 1500s,</p>
<div class="btn hero-btn">Free Consult Now</div>
<svg class="abs" style="left:0;top:640px" width="1200" height="120" viewBox="0 0 1200 120">
  <path d="M0 50 Q600 -20 1200 50 L1200 120 L0 120Z" fill="var(--green)"/>
  <path d="M0 60 Q600 -5 1200 70 L1200 120 L0 120Z" fill="var(--green-light)"/>
  <path d="M0 112 Q600 30 1200 110 L1200 120 L0 120Z" fill="#fff"/>
</svg>
<div class="abs dots"><span></span><span class="on"></span><span></span></div>

<!-- about -->
<section>
  <div class="abs eyebrow about-eyebrow">About Us</div>
  <h2 class="abs about-title slab">Verdano</h2>
  <div class="abs about-text">
    <p>Lorem Ipsum is simply dummy text of the printing and typesetting industry. Lorem Ipsum has been the industry's standard dummy text ever since the 1500s, when an unknown printer took a galley of type and scrambled it to make a type specimen book.</p>
    <p>It has survived not only five centuries, but also the leap into electronic typesetting, remaining essentially unchanged.</p>
  </div>
  <div class="btn about-btn">Read More</div>
  <div class="abs" style="left:792px;top:880px;width:190px;height:325px;border-radius:95px;background:linear-gradient(180deg,var(--green-light),var(--green))"></div>
  <div class="abs about-photo" role="img" aria-label="Business colleagues talking in an office" style="left:614px;top:808px;width:232px;height:396px;background:linear-gradient(160deg,#d9dcd6,#8a8f88);border:5px solid #fff"></div>
  <div class="abs about-photo" role="img" aria-label="Advisor meeting with a client at a table" style="left:855px;top:878px;width:232px;height:326px;background:linear-gradient(160deg,#cfd6d8,#6f7677);border:5px solid #fff"></div>
</section>

<!-- services -->
<section>
  <div class="abs services-bg" role="img" aria-label="Hands working on a calculator and paperwork, darkened"></div>
  <svg class="abs" style="left:0;top:1285px" width="1200" height="60" viewBox="0 0 1200 60"><path d="M0 0 H1200 V8 Q600 70 0 8Z" fill="#fff"/></svg>
  <div class="abs eyebrow services-eyebrow">We Offers</div>
  <h2 class="abs services-title slab">Services Include</h2>
  <div class="abs services-underline"></div>
  <p class="abs services-text">Lorem Ipsum is simply dummy text of the printing and typesetting industry. Lorem Ipsum has been the industry's standard dummy text ever since the 1500s, when an unknown printer took.</p>
  <div class="abs" style="left:0;top:1987px;width:1200px;height:80px;background:#fff"></div>

  <div class="abs card" style="left:112px;background:linear-gradient(180deg,#3a3a3a 0%,#1a1a1a 70%,#000 100%)" role="img" aria-label="Tax forms and calculator">
    <div class="label">Tax Services <span class="arrow"><svg width="14" height="14" viewBox="0 0 14 14"><path d="M3 11 L11 3 M5 3 H11 V9" stroke="#222" stroke-width="2" fill="none"/></svg></span></div>
  </div>
  <div class="abs card card-consult" style="left:448px">
    <h3>Consulting</h3>
    <ul><li>Entity Selection &amp; Restructuring</li><li>Financial Projections &amp; Forecasts</li><li>Retirement Planning</li><li>IPO Readiness</li></ul>
    <div class="arrow"><svg width="14" height="14" viewBox="0 0 14 14"><path d="M3 11 L11 3 M5 3 H11 V9" stroke="#222" stroke-width="2" fill="none"/></svg></div>
  </div>
  <div class="abs card" style="left:784px;background:linear-gradient(180deg,#dfe4ea 0%,#8c95a0 60%,#000 100%)" role="img" aria-label="Accountant working with documents at a desk">
    <div class="label">Accounting <span class="arrow"><svg width="14" height="14" viewBox="0 0 14 14"><path d="M3 11 L11 3 M5 3 H11 V9" stroke="#222" stroke-width="2" fill="none"/></svg></span></div>
  </div>
  <div class="btn services-btn">View More</div>
</section>

<!-- why + contact -->
<section>
  <div class="abs why" role="img" aria-label="Dark financial workspace backdrop">
    <h2 class="slab">Why Settle for less<br>when your <em>Finances<br>could be Exact?</em></h2>
    <div class="feature" style="top:235px"><span class="ic"><svg width="30" height="30" viewBox="0 0 30 30"><circle cx="15" cy="15" r="7" fill="none" stroke="#222" stroke-width="3"/><circle cx="15" cy="15" r="2" fill="#222"/></svg></span>Experienced</div>
    <div class="feature" style="top:325px"><span class="ic"><svg width="30" height="30" viewBox="0 0 30 30"><circle cx="15" cy="13" r="8" fill="none" stroke="#222" stroke-width="3"/><path d="M10 20 L8 28 L15 25 L22 28 L20 20" fill="#222"/></svg></span>Professional</div>
    <div class="feature" style="top:410px"><span class="ic"><svg width="30" height="30" viewBox="0 0 30 30"><path d="M4 22 H12 L20 18 Q24 17 22 21 L14 26 H4Z" fill="#222"/><circle cx="17" cy="10" r="5" fill="#222"/></svg></span>Affordable</div>
  </div>
  <div class="abs contact" role="img" aria-label="Green tinted financial charts backdrop">
    <h3>GET IN TOUCH</h3>
    <div class="bar"></div>
  </div>
  <div class="field" style="left:621px;top:2473px;width:218px">Your name</div>
  <div class="field" style="left:848px;top:2473px;width:218px">Phone</div>
  <div class="field" style="left:621px;top:2523px;width:218px">Email address</div>
  <div class="field" style="left:848px;top:2523px;width:218px">Subject</div>
  <div class="field" style="left:621px;top:2574px;width:445px;height:72px">Message</div>
  <div class="submit" style="left:621px">SUBMIT</div>
</section>

<!-- news -->
<section>
  <h2 class="abs news-title slab">LATEST NEWS/PRESS<br>RELEASES</h2>
  <article class="abs news-card" style="left:0;width:306px;height:498px">
    <div class="img" role="img" aria-label="Person viewing a financial report with charts" style="background:linear-gradient(160deg,#e3edf5,#8fa6bd)"></div>
    <span class="date">Jul 19, 2023</span>
    <h4 style="font-size:18px;line-height:30px">Sed ut perspiciatis unde omnis iste natus error sit voluptatem</h4>
  </article>
  <article class="abs news-card" style="left:341px;width:518px;height:498px">
    <div class="img" role="img" aria-label="Hands signing documents beside a calculator" style="background:linear-gradient(160deg,#c9ccd0,#5f656b)"></div>
    <span class="date">Jul 19, 2023</span>
    <h4 style="font-size:27px;line-height:36px;padding:18px 40px 0">Sed ut perspiciatis unde omnis iste natus error sit voluptatem</h4>
  </article>
  <article class="abs news-card" style="left:895px;width:305px;height:498px">
    <div class="img" role="img" aria-label="Businesswoman reading a document" style="background:linear-gradient(160deg,#e9e6e2,#9b8f86)"></div>
    <span class="date">Jul 19, 2023</span>
    <h4 style="font-size:18px;line-height:30px">Sed ut perspiciatis unde omnis iste natus error sit voluptatem</h4>
  </article>
  <div class="btn news-btn">View More</div>
</section>

<!-- footer -->
<footer>
  <div class="abs footer-bg" role="img" aria-label="Faint dark financial chart backdrop"></div>
  <svg class="abs" style="left:0;top:3800px" width="1200" height="110" viewBox="0 0 1200 110">
    <path d="M0 0 H1200 V10 Q600 150 0 10Z" fill="#fff"/>
    <path d="M0 10 Q600 150 1200 10 V30 Q600 170 0 40Z" fill="var(--green-light)"/>
    <path d="M0 40 Q600 170 1200 30 V45 Q600 175 0 55Z" fill="var(--green)"/>
  </svg>
  <div class="abs brand foot-brand"><span class="dot"></span>VERDANO</div>
  <div class="abs foot-col" style="left:480px;top:3994px;width:250px">
    <h5>TO REACH US</h5>
    <div class="reach"><span class="ic"><svg width="16" height="18" viewBox="0 0 16 18"><path d="M8 17 C3 11 2 9 2 7 A6 6 0 0 1 14 7 C14 9 13 11 8 17Z" fill="none" stroke="#ffd200" stroke-width="1.6"/><circle cx="8" cy="7" r="2" fill="#ffd200"/></svg></span><div>VERDANO<br>418 C 12 Street Lindel, ON,<br>Canada K2R 4P9</div></div>
    <div class="reach"><span class="ic"><svg width="16" height="16" viewBox="0 0 16 16"><path d="M3 2 L6 2 L7 6 L5 7 Q6 10 9 11 L10 9 L14 10 L14 13 Q8 15 2 6Z" fill="none" stroke="#ffd200" stroke-width="1.5"/></svg></span><div>PHONE: (555) 204-3187<br>FAX: (555) 204-3190</div></div>
    <div class="reach"><span class="ic"><svg width="18" height="14" viewBox="0 0 18 14"><rect x="1" y="1" width="16" height="12" fill="none" stroke="#ffd200" stroke-width="1.5"/><path d="M1 1 L9 8 L17 1" fill="none" stroke="#ffd200" stroke-width="1.5"/></svg></span><div>EMAIL:<br>hello@verdano-example.com</div></div>
  </div>
  <div class="abs foot-col" style="left:757px;top:3994px">
    <h5>QUICK LINKS</h5>
    <ul><li>Home</li><li>About Us</li><li>What We Do</li><li>Latest News</li><li>Contact Us</li></ul>
  </div>
  <div class="abs foot-col" style="left:957px;top:3994px">
    <h5>SERVICES</h5>
    <ul><li>Tax Services</li><li>Consulting</li><li>Accounting</li><li>CFO Services</li><li>Compliance Services</li><li>Controller Services</li></ul>
  </div>
  <div class="abs copyright">Verdano © 2023 All Rights Reserved.</div>
  <div class="abs social"><span></span><span></span><span></span><span></span><span></span></div>
</footer>

</body>
</html>
```